A4 Tri-fold Brochure for Sedation Dentist Specialist Dr. Orrin and Sedation Dentistry.

I would like to create an A4 tri-fold brochure for our Dental Sedation Specialist Dr. Orrin Lask. Please carefully select the most suitable highlights from his bio below.

This brochure has two parts. Highlighting what makes Dr. Orrin Lask unique and trustworthy. Include a picture of him (attached). The second part is about sedation dentistry. All you need to know here: http://www.calmchairhub.example/how-does-sedation-dentistry-work

Avoid making it too wordy.

Meet Dr. Ruo Fen Orrin Lask, DDS

Inspired to Become a Dentist:
As a child, Dr. Orrin Lask always felt stressed whenever he had to see a dentist. He knew that he wanted to become a dentist to help put patients completely at ease while they experienced quality dental care.

He is passionate about giving patients the healthy, beautiful smiles they deserve. “I find it fulfilling when I can see my patients’ beautiful smiles and how they can finally appreciate the joy of eating with a healthy set of teeth. However, what I love most about my job is the ability to provide a stress-free and comfortable experience at the dentist’s office, particularly for children, through sedation and general anesthesia.”

Educational Achievements:
Before becoming a dentist, Dr. Orrin Lask earned his undergraduate degree at the University of Greybrook Valley where he received a Bachelor of Medical Science Honor Specialization degree with distinction in biochemistry. He then completed his Doctor of Dental Surgery degree with honors at the University of Marrowfield. While there, he received the Edmund Tarrow Medal in his class for outstanding achievement in anesthesia. He then pursued his three-year residency as well as a master’s degree in dental anesthesia at the University of Marrowfield.

So he can provide his patients with the latest in dentistry, Dr. Orrin Lask enjoys pursuing additional knowledge, particularly in the areas of dental anesthesia as well as advanced technologies in dentistry. He is currently part of the Bracken Molar Circle study club and has enrolled in the Basic Implant Mini- Residency Track. He also serves as a clinical instructor at the Plexor Clinic at the University of Marrowfield.

Association Memberships:
In addition to his academic credentials, Dr. Orrin Lask is a member of several associations:
The Chartered Guild of Dental Surgeons of Norvale (CGDSN)
Dental Continental Union of Dental Anesthesia (CUDA)
Northland Institute of Dental Anesthesia (NIDA)
Norvale Dental Federation (NDF)
Outside the Practice

When he’s not at the practice, Dr. Orrin Lask enjoys spending time with his wife Marla and their two poodles Pip and Tofu, who are spoiled rotten! “Marla and I love taking our dogs out on hikes and to the dog park on weekends. I also enjoy a wide range of activities from model building and playing the piano to soccer, gym and archery.” He stays fit by working out at the local Strivo gym, and he likes to walk in Larkbend Creek Park and Ashcombe Meadow Park.

Dr. Orrin Lask considers himself to be a kid at heart. He is a big fan of superheroes and animated movies. “I get really excited about any upcoming superhero or Vellum Brightframe movies. Till this day, I still collect superhero toy figures.”

He supports the BrightWard Trust as well as the Norvale League for the Protection of Creatures (LPC).

Experience outstanding dental care with our highly skilled dentist. Contact us today to schedule an appointment with Dr. Orrin Lask! He speaks English, Cantonese, and Mandarin.

Target Market(s)

Mothers with young kids.

Industry/Entity Type

Dental

Font styles to use
Sans Serif

Requirements
Should not have
• Prices

```html
<!DOCTYPE html>
<html lang="en">
<head>
<meta charset="utf-8">
<title>Dr. Orrin Lask – Sedation Dentistry Brochure (Inside)</title>
<link rel="stylesheet" href="https://fonts.googleapis.com/css2?family=Marcellus&family=Marcellus+SC&display=swap">
<style>
  :root {
    --navy: #0f2f6e;
    --teal: #1aa58f;
    --teal-light: #2bbfa6;
    --ink: #ffffff;
  }
  * { box-sizing: border-box; margin: 0; padding: 0; }
  html, body { width: 1200px; height: 849px; overflow: hidden; background: #ffffff; }
  .brochure { position: relative; width: 1200px; height: 849px; overflow: hidden; color: var(--ink); }
  .brochure__backdrop { position: absolute; inset: 0; width: 1200px; height: 849px; }
  .section { position: absolute; }
  .section__title {
    font-family: "Marcellus", serif;
    font-weight: 400;
    font-size: 19px;
    letter-spacing: 0.5px;
    text-align: center;
    line-height: 1.2;
    margin-bottom: 14px;
  }
  .section p, .section li {
    font-family: "Marcellus SC", serif;
    font-size: 8.6px;
    line-height: 1.27;
    text-transform: uppercase;
    text-align: justify;
    letter-spacing: 0.1px;
  }
  .section p { text-indent: 16px; margin-bottom: 9px; }
  .section p.plain { text-indent: 0; }
  .members { list-style: none; margin: 2px 0 0; }
  .members li { text-align: left; padding-left: 10px; position: relative; }
  .members li::before { content: "·"; position: absolute; left: 0; }
  .col-left { left: 32px; width: 360px; }
  .col-mid { left: 440px; width: 370px; }
  .col-right { left: 836px; width: 336px; }
  .divider-ornament {
    position: absolute; left: 176px; top: 566px; width: 70px; height: 18px;
    background: rgba(255,255,255,0.85); border-radius: 50%;
  }
</style>
</head>
<body>
<main class="brochure">
  <svg class="brochure__backdrop" viewBox="0 0 1200 849" aria-hidden="true">
    <rect width="1200" height="849" fill="var(--teal)"/>
    <polygon points="0,0 1200,0 1200,18 0,30" fill="var(--teal-light)"/>
    <polygon points="0,28 770,28 800,18 1200,18 1200,812 430,812 398,822 0,822" fill="var(--navy)"/>
    <polygon points="0,836 1200,826 1200,849 0,849" fill="var(--teal-light)"/>
  </svg>

  <!-- Left panel -->
  <section class="section col-left" style="top:50px">
    <h2 class="section__title">Educational Achievements</h2>
    <p>Before becoming a dentist, Dr. Orrin Lask earned his undergraduate degree at the University of Greybrook Valley where he received a Bachelor of Medical Science Honor Specialization degree with distinction in biochemistry. He then completed his Doctor of Dental Surgery degree with honors at the University of Marrowfield. While there, he received the Edmund Tarrow Medal in his class for outstanding achievement in anesthesia. He then pursued his three-year residency as well as a master's degree in dental anesthesia at the University of Marrowfield. So he can provide his patients with the latest in dentistry, Dr. Orrin Lask enjoys pursuing additional knowledge, particularly in the areas of dental anesthesia as well as advanced technologies in dentistry. He is currently part of the Bracken Molar Circle study club and has enrolled in the Basic Implant Mini- Residency Track. He also serves as a clinical instructor at the Plexor Clinic at the University of Marrowfield.</p>
  </section>

  <section class="section col-left" style="top:240px">
    <h2 class="section__title">Association Memberships</h2>
    <p class="plain">In addition to his academic credentials, Dr. Orrin Lask is a member of several associations:</p>
    <ul class="members">
      <li>The Chartered Guild of Dental Surgeons of Norvale (CGDSN)</li>
      <li>Dental Continental Union of Dental Anesthesia (CUDA)</li>
      <li>Northland Institute of Dental Anesthesia (NIDA)</li>
      <li>Norvale Dental Federation (NDF)</li>
    </ul>
  </section>

  <section class="section col-left" style="top:356px">
    <h2 class="section__title">Outside the Practice</h2>
    <p>When he's not at the practice, Dr. Orrin Lask enjoys spending time with his wife Marla and their two poodles Pip and Tofu, who are spoiled rotten! "Marla and I love taking our dogs out on hikes and to the dog park on weekends. I also enjoy a wide range of activities from model building and playing the piano to soccer, gym and archery." He stays fit by working out at the local Strivo gym, and he likes to walk in Larkbend Creek Park and Ashcombe Meadow Park. Dr. Orrin Lask considers himself to be a kid at heart. He is a big fan of superheroes and animated movies. "I get really excited about any upcoming superhero or Vellum Brightframe movies. Till this day, I still collect superhero toy figures." He supports the BrightWard Trust as well as the Norvale League for the Protection of Creatures (LPC). Experience outstanding dental care with our highly skilled dentist. Contact us today to schedule an appointment with Dr. Orrin Lask! He speaks English, Cantonese, and Mandarin.</p>
  </section>

  <div class="divider-ornament" role="img" aria-label="Decorative flourish divider"></div>

  <section class="section col-left" style="top:606px">
    <h2 class="section__title">About oral sedation</h2>
    <p>Oral sedation dentistry allows appropriately trained dentists to create a safe and comfortable dental experience for patients who have avoided the dentist out of fear or who might have time restrictions.</p>
    <p class="plain">A dentist who has been trained to implement sedation can effectively helping a patient become as comfortable and relaxed as possible using well established and proven protocols with a variety of sedation medications administered orally and sublingually (under the tongue). These protocols can be customized for the patient's individual emotional and physical needs.</p>
    <p class="plain">Sometimes referred to as 'relaxation', 'sleep' or 'anxiety free' dentistry, this comfortable care is now offered by thousands of trained dentists all over the US and Canada.</p>
  </section>

  <!-- Middle panel -->
  <section class="section col-mid" style="top:34px">
    <p>Oral conscious sedation has provided access to care for hundreds of thousands of Americans who otherwise would have been without the dental care they need. Dentists who have received comprehensive training from the Calm Care Sedation Council have an amazing tool to treat patients safely and comfortably, often correcting years of professional neglect in just a few visits. No longer does fear, or the inconvenience of having multiple visits, have to be the overwhelming obstacle that it has been in the past. When it comes to the impact on the dental health of the United States, conscious sedation dentistry stands as one of the most meaningful advances of the past century." —Lorna T Vesk, DMD; Dean CCSC Faculty.</p>
  </section>

  <section class="section col-mid" style="top:202px">
    <h2 class="section__title">What is Sedative?</h2>
    <p>Sedative medication helps relax patients by slowing the action of the central nervous system. People remain aware of their surroundings, but are less responsive to external stimuli like the sound of the drill or the smell of materials.</p>
    <p>This also reduces their sense of pain. Sedatives aren't new; in fact, they date back thousands of years. Pain management is as old as medicine, and other ancient forms include alcohol, the mandrake root and opium poppies. The modern age of sedative medication began in the 1800s with the creation of bromides and chloral hydrate.</p>
    <p>Today's doctor draws upon a continually-expanding list of new sedatives to help lessen pain and dental anxiety. Current medications are often more powerful and less likely to carry unpleasant side effects. However, all medications differ, and there's no one medication that's appropriate for every patient. Some of the drugs take action quickly but rapidly fade in potency, while others last for hours. Doctors weigh a number of factors carefully to assess which drug will be the safest choice in a unique situation for a particular individual.</p>
  </section>

  <section class="section col-mid" style="top:462px">
    <h2 class="section__title">What is pediatric<br>sedation dentistry?</h2>
    <p>Adult sedation dentistry has grown in popularity over the last fifteen years and was developed as a way to reduce or eliminate much of the fear or anxiety many adults experience upon visiting the dentist. Pediatric sedation is the unique study and implementation of sedation for children aged 5-12. It allows appropriately trained dentists to create safe and comfortable dental experiences for children who have avoided the dentist out of fear. A dentist who has been trained to implement pediatric sedation can effectively help a patient become as comfortable and relaxed as possible using well established and proven protocols with a variety of sedation medications administered orally and sublingually (under the tongue). This approach also prevents children fromdeveloping a fear of the dentist by creating great experiences.</p>
    <p>Although children have the same fears and reservations towards the dentist as adults often do, pediatric sedation dentists must be trained specifically to treat children – not just adults. Children have a largely distinct set of needs. They have different airways than adults and, of course, different rates of metabolizing sedatives. Therefore, pediatric dentists must complete a unique curriculum in order to perform pediatric sedation.</p>
    <p>As a parent, it's important to research pediatric sedation fully to know if it is the right choice for you and your child. Below are some common questions parents and children may have prior to considering pediatric sedation dentistry.</p>
  </section>

  <!-- Right panel -->
  <section class="section col-right" style="top:60px">
    <h2 class="section__title">What is pediatric<br>sedation</h2>
    <p>Anyone who has taken their child to the dentist for consecutive appointments knows the - ahem - drill. And if your child is like most kids (with an attention span no longer than a Maple Lane episode) then no amount of prizes from the prize basket will alleviate their unhappiness.</p>
    <p>To put it plainly, going to the dentist can be even more taxing for kiddos than for us grownups. So what's a parent to do?</p>
    <p>There's a way to help: pediatric sedation dentistry.</p>
    <p>"The phobia that many adults have today regarding dental treatment is often the result of poor dental experiences when they were children. Children today receiving invasive dental treatment can be treated as they would if they received invasive medical treatment – with safe orally administered sedation. Utilizing modern, safe sedative medications, a child can be conscious, yet sleepy, with no memory of their dental treatment. With proper case selection, utilization of monitoring equipment, and established emergency preventative and preparedness protocols, a properly trained dentist and team can safely perform oral conscious sedation on appropriate children in the dental practice. Children today can grow up without unpleasant memories of going to the dentist and enjoy a trusting, positive relationship withdentist and team for the rest of their lives." —Dale Winthrop, DDS, MS</p>
  </section>

  <section class="section col-right" style="top:422px">
    <h2 class="section__title">What is IV sedation dentistry?</h2>
    <p>IV stands for intravenous. Medication that is administered intravenously is administered through the veins. Because of its rapid effects many patients prefer this option.</p>
    <p>"Providing sedation to dental patients is a commitment to the highest level of comfortable care, including sedation provided through Intravenous Sedation (IV).. Patients are surprised at how easy it is and how relaxed they are during the procedure. They are impressed with doctors who have received this level of sedation training and offer an alternative for those who may not be comfortable with oral sedation. Many who receive IV sedation eventually find that for routine procedures they do not need sedation anymore. Patients who have treatment provided by a CCSC-trained dentist are assured to have a comfortable, pleasant sedation experience." —RK Fenmore, DDS; Clinical Professor at Eastmoor University.</p>
  </section>

  <section class="section col-right" style="top:650px">
    <h2 class="section__title">What is nitrous oxide?</h2>
    <p>What is nitrous oxide?Nitrous oxide is an odorless and colorless gas. In the early 1800s a British scientist found that inhaling nitrous produces highly pleasurable sensations. New York dentist Edmund Tarrow learned in 1844 that nitrous could distract patients from acute pain such as the type associated with tooth extraction. Dentistry has relied upon nitrous oxide ever since then, but the techniques, type of gas mixture and delivery methods have been greatly improved.y.</p>
  </section>
</main>
</body>
</html>
```